Lumo4Kart - a fintech company - business card

We need a business card design for our Payments Technology company in Sydney, Australia. We provide business with payment solutions expanding across EFTPOS machines, online payment gateways and mobile payment solutions. We would like to see designs that are clean, classy and professional.
Target Market(s)
Business professionals, executives, c-suite
Industry/Entity Type
Fintech
Contact Information for Business Card
Will be on 400gsm. Logo will most likely be spot gloss unless designer recommends otherwise.
Font styles to use
Sans Serif
Requirements
Must have
- We need our website (lumo4kart.com.au), email (contact@lumo4kart.com.au), mobile (0432 587 904) and direct phone number (02 6815 3927) to feature on the card along with our logo (attached) and the words "EFTPOS | ONLINE | MOBILE"
- Font = Roboto

```html
<!DOCTYPE html>
<html lang="en">
<head>
<meta charset="utf-8">
<title>Lumo4Kart – Business Card</title>
<link href="https://fonts.googleapis.com/css2?family=Roboto:wght@400;500;700&display=swap" rel="stylesheet">
<style>
  :root {
    --bg: #2a2a2c;
    --brand-blue: #23649c;
    --brand-blue-light: #3272aa;
    --brand-grey: #626469;
    --text-grey: #55575c;
    --paper: #ffffff;
    --paper-shade: #f3f4f5;
  }
  * { box-sizing: border-box; margin: 0; padding: 0; }
  html, body {
    width: 1200px; height: 900px; overflow: hidden;
    background: var(--bg);
    font-family: "Roboto", Arial, sans-serif;
  }
  .stage { position: relative; width: 1200px; height: 900px; }
  .card {
    position: absolute; width: 640px; height: 390px;
    box-shadow: 0 18px 40px rgba(0,0,0,.55);
    overflow: hidden;
  }
  /* back side */
  .card-back {
    left: 320px; top: 45px;
    background: linear-gradient(135deg, var(--brand-blue) 0%, var(--brand-blue-light) 100%);
    color: var(--paper);
  }
  .card-back .brand-disc {
    position: absolute; left: 40px; top: 20px;
    width: 330px; height: 330px; border-radius: 50%;
    background: var(--paper);
  }
  .card-back .wordmark {
    position: absolute; right: 34px; top: 40px;
    font-size: 34px; font-weight: 700; letter-spacing: .5px;
  }
  .card-back .services {
    position: absolute; right: 34px; bottom: 34px;
    font-size: 22px; font-weight: 400; letter-spacing: 1.5px;
  }
  /* front side */
  .card-front {
    left: 240px; top: 470px;
    background: linear-gradient(180deg, var(--paper) 0%, var(--paper-shade) 100%);
  }
  .card-front .waves { position: absolute; inset: 0; }
  .logo-lockup {
    position: absolute; left: 30px; top: 70px; width: 270px;
    display: flex; flex-direction: column; align-items: center;
  }
  .logo-lockup .mark-dot {
    width: 96px; height: 96px; border-radius: 50%;
    background: var(--brand-blue); margin-bottom: 16px;
  }
  .logo-lockup .wordmark {
    font-size: 40px; font-weight: 700; color: var(--brand-grey); letter-spacing: .3px;
  }
  .divider {
    position: absolute; left: 312px; top: 92px; width: 2px; height: 160px;
    background: var(--brand-grey);
  }
  .contact-block { position: absolute; left: 336px; top: 95px; }
  .contact-block .person-name {
    font-size: 24px; font-weight: 700; color: var(--brand-blue); line-height: 1;
  }
  .contact-block .person-title {
    font-size: 18px; color: var(--text-grey); margin-top: 4px; margin-bottom: 14px;
  }
  .contact-list { list-style: none; }
  .contact-list li {
    display: flex; align-items: center; gap: 12px;
    font-size: 17px; color: var(--text-grey); height: 23px;
  }
  .contact-list svg { width: 17px; height: 17px; fill: var(--brand-blue); flex: none; }
</style>
</head>
<body>
<main class="stage">

  <section class="card card-back" aria-label="Business card back">
    <div class="brand-disc"></div>
    <div class="wordmark">LUMO4KART</div>
    <div class="services">EFTPOS | ONLINE | MOBILE</div>
  </section>

  <section class="card card-front" aria-label="Business card front">
    <svg class="waves" viewBox="0 0 640 390" preserveAspectRatio="none" aria-hidden="true">
      <path d="M0 258 C40 305 220 330 470 330 C240 336 50 322 0 292 Z" fill="var(--brand-grey)"/>
      <path d="M0 305 C90 345 290 350 440 343 C540 338 600 318 640 292 L640 390 L0 390 Z" fill="var(--brand-blue)"/>
    </svg>

    <div class="logo-lockup">
      <div class="mark-dot"></div>
      <div class="wordmark">LUMO4KART</div>
    </div>

    <div class="divider"></div>

    <div class="contact-block">
      <div class="person-name">YOUR NAME</div>
      <div class="person-title">Your Title</div>
      <ul class="contact-list">
        <li>
          <svg viewBox="0 0 24 24"><path d="M6.6 10.8a15.1 15.1 0 0 0 6.6 6.6l2.2-2.2c.3-.3.7-.4 1-.2 1.1.4 2.3.6 3.6.6.6 0 1 .4 1 1V20c0 .6-.4 1-1 1C10.6 21 3 13.4 3 4c0-.6.4-1 1-1h3.5c.6 0 1 .4 1 1 0 1.3.2 2.5.6 3.6.1.3 0 .7-.2 1z"/></svg>
          0432 587 904
        </li>
        <li>
          <svg viewBox="0 0 24 24"><path d="M7 1h10a2 2 0 0 1 2 2v18a2 2 0 0 1-2 2H7a2 2 0 0 1-2-2V3a2 2 0 0 1 2-2zm0 3v14h10V4zm5 15.5a1.2 1.2 0 1 0 0 2.4 1.2 1.2 0 0 0 0-2.4z"/></svg>
          02 6815 3927
        </li>
        <li>
          <svg viewBox="0 0 24 24"><path d="M2 5h20v14H2zm2 2v.4l8 5.3 8-5.3V7zm0 2.8V17h16V9.8l-8 5.3z"/></svg>
          contact@lumo4kart.com.au
        </li>
        <li>
          <svg viewBox="0 0 24 24"><path d="M12 2a10 10 0 1 0 0 20 10 10 0 0 0 0-20zm0 2c1 0 2.3 2 2.8 5H9.2C9.7 6 11 4 12 4zM4.3 11h3.8c0 1.4.1 2.7.4 4H5a8 8 0 0 1-.7-4zm4.9 6h5.6c-.5 2-1.6 3-2.8 3s-2.3-1-2.8-3zm-.1-6h5.8c0 1.4-.1 2.8-.4 4H9.5c-.3-1.2-.4-2.6-.4-4zm6.8 0h3.8a8 8 0 0 1-.7 4h-3.5c.3-1.3.4-2.6.4-4z"/></svg>
          lumo4kart.com.au
        </li>
      </ul>
    </div>
  </section>

</main>
</body>
</html>
```